Email Newsletter Banner

I require 2 new email newsletter and web banners to be made up.
I require the brand names to be included on the banner which are " Wire Dispatcher" and "PC Flashz". I would also like some sort of imagery and also a "sign up here" button. Please see below examples:
https://dataskyreports.lornexhub.com/
https://datawisdomsky.lornexhub.com/
https://datastoryvault.lornexhub.com/

```html
<!DOCTYPE html>
<html lang="en">
<head>
<meta charset="utf-8">
<title>PC Flashz – Newsletter Banner</title>
<link rel="stylesheet" href="https://fonts.googleapis.com/css2?family=Poppins:ital,wght@0,800;1,700&display=swap">
<style>
  :root {
    --page: #ffffff;
    --navy-deep: #0a2450;
    --navy: #123a7a;
    --blue-mid: #1a5aa6;
    --globe-dark: #06305a;
    --globe-light: #5cc8e6;
    --wordmark: #f1f1f1;
    --button-violet: #7b2fe0;
    --button-blue: #2a9bd6;
    --button-edge: #ffffff;
    --chevron-box: #1a1f4a;
  }
  * { margin: 0; padding: 0; box-sizing: border-box; }
  html, body {
    width: 1200px;
    height: 275px;
    overflow: hidden;
    background: var(--page);
  }
  .banner {
    position: absolute;
    left: 10px;
    top: 10px;
    width: 1176px;
    height: 257px;
    overflow: hidden;
    background: linear-gradient(100deg, var(--navy) 0%, var(--navy-deep) 30%, var(--blue-mid) 48%, var(--navy-deep) 70%, var(--navy-deep) 100%);
  }
  .backdrop-art {
    position: absolute;
    inset: 0;
    background: radial-gradient(ellipse at 20% 50%, rgba(60,120,210,0.35), transparent 60%);
  }
  .globe-art {
    position: absolute;
    left: 683px;
    top: -111px;
    width: 500px;
    height: 500px;
    border-radius: 50%;
    background: radial-gradient(circle at 72% 45%, var(--globe-light) 0%, #2a86b8 35%, var(--globe-dark) 75%);
    box-shadow: 0 0 40px rgba(92,200,230,0.45);
  }
  .wordmark {
    position: absolute;
    left: 40px;
    top: 62px;
    font-family: "Poppins", sans-serif;
    font-weight: 800;
    font-size: 96px;
    line-height: 1;
    letter-spacing: 1px;
    color: var(--wordmark);
    text-transform: uppercase;
    white-space: nowrap;
  }
  .signup-button {
    position: absolute;
    left: 456px;
    top: 171px;
    width: 192px;
    height: 28px;
    display: flex;
    align-items: center;
    transform: skewX(-12deg);
    border: 2px solid var(--button-edge);
    background: linear-gradient(90deg, var(--button-violet) 0%, var(--button-blue) 100%);
    text-decoration: none;
  }
  .signup-chevron {
    width: 28px;
    height: 100%;
    background: var(--chevron-box);
    display: flex;
    align-items: center;
    justify-content: center;
  }
  .signup-chevron svg { transform: skewX(12deg); }
  .signup-label {
    flex: 1;
    text-align: center;
    transform: skewX(12deg);
    font-family: "Poppins", sans-serif;
    font-style: italic;
    font-weight: 700;
    font-size: 18px;
    color: #ffffff;
    letter-spacing: -0.3px;
  }
</style>
</head>
<body>
  <div class="banner">
    <div class="backdrop-art" role="img" aria-label="Blue circuit-board line pattern in the background"></div>
    <div class="globe-art" role="img" aria-label="Glowing blue digital globe showing the Americas and Africa with grid lines"></div>
    <div class="wordmark">PC Flashz</div>
    <a class="signup-button" href="#">
      <span class="signup-chevron">
        <svg width="10" height="14" viewBox="0 0 10 14"><path d="M2 1 L8 7 L2 13" fill="none" stroke="#ffffff" stroke-width="2"/></svg>
      </span>
      <span class="signup-label">SIGN UP HERE</span>
    </a>
  </div>
</body>
</html>
```